Business Card for Hollin Ledger - A cannabis publication for executives.

I'd like some business cards for Hollin Ledger. The logo is done (great job!) and I need a card design I will use with PELT. I made it a short project to allow time for printing before an event. These will be standard sized cards (final artwork size 3.66" x 2.16" at 300dpi) with a final card size of 3.5" x 2.0". (See PELT.example if you need more info.) I might try rounded corners but am not sure yet. I think the design will work okay with rounded.

Hollin Ledger will be a bi-weekly publication for the cannabis industry. It is targeted to investors and industry executives, not consumers or pot smokers. So our market is more B2B. However I am open to creativity and making the card something people remark on.

My contact for card:

Dara Venholm
Founder/CEO
dara@hollinledger.example

2746 Marrow Lane
Boston MA 02391
(617)555-0193

Target Market(s)

Executives, Industry people and investors in the Cannabis sector.

Contact Information for Business Card

PELT does do double sided and the second side can be the same or different images. Only one side is required but use of the second side would be a bonus.

Font styles to use
Serif
Sans Serif
Decorative

Colors

Designer to choose colors to be used in the design.

Requirements
Must have
• Logo, contact info
Nice to have
• Style and design to make the card stand out in a crowd.

```html
<!DOCTYPE html>
<html lang="en">
<head>
<meta charset="utf-8">
<title>Hollin Ledger – Business Card</title>
<link rel="stylesheet" href="https://fonts.googleapis.com/css2?family=Open+Sans:wght@400;600;700&display=swap">
<style>
  :root {
    --brand-blue: #1175bd;
    --brand-green: #7bab2f;
    --ink: #4a4a4a;
    --rule: #8a8a8a;
    --card-white: #ffffff;
    --backdrop: #e9e6e1;
  }
  * { margin: 0; padding: 0; box-sizing: border-box; }
  html, body {
    width: 1200px; height: 987px; overflow: hidden;
    background: var(--backdrop);
    font-family: "Open Sans", Arial, sans-serif;
  }
  .card {
    position: absolute; left: 292px; width: 616px; height: 352px;
    box-shadow: 0 3px 10px rgba(0,0,0,0.25);
    overflow: hidden;
  }
  .card--front { top: 132px; background: var(--card-white); }
  .card--back { top: 507px; background: var(--brand-blue); }

  .wordmark {
    position: absolute; display: flex; align-items: center; gap: 12px;
    font-weight: 600; white-space: nowrap;
  }
  .wordmark__mark { display: block; }
  .card--front .wordmark { right: 31px; top: 46px; font-size: 40px; color: var(--brand-blue); }
  .card--front .wordmark__mark { width: 34px; height: 34px; background: var(--brand-green); }
  .card--back .wordmark {
    left: 50%; top: 50%; transform: translate(-50%, -50%);
    font-size: 52px; color: var(--card-white);
  }
  .card--back .wordmark__mark { width: 46px; height: 46px; background: var(--card-white); }

  .person { position: absolute; left: 34px; top: 192px; }
  .person__name { font-size: 21px; font-weight: 700; color: var(--brand-blue); letter-spacing: 0.3px; line-height: 1.2; }
  .person__title { font-size: 15.5px; color: var(--brand-green); line-height: 1.3; }

  .divider { position: absolute; left: 34px; top: 244px; width: 551px; height: 1px; background: var(--rule); }

  .contact { position: absolute; left: 34px; top: 252px; font-size: 15px; color: var(--ink); line-height: 24px; }
  .contact__row { display: flex; align-items: center; gap: 8px; }
  .contact__icon { width: 14px; height: 14px; fill: var(--brand-blue); }

  .address { position: absolute; right: 31px; top: 252px; text-align: right; font-size: 15px; color: var(--ink); line-height: 24px; }

  .footer-band { position: absolute; left: 0; bottom: 0; }
  .website {
    position: absolute; right: 31px; bottom: 10px;
    font-size: 14.5px; letter-spacing: 2.6px; color: var(--card-white);
  }
</style>
</head>
<body>
  <section class="card card--front" aria-label="Card front">
    <div class="wordmark"><span class="wordmark__mark"></span>Hollin Ledger</div>

    <div class="person">
      <div class="person__name">DARA VENHOLM</div>
      <div class="person__title">Founder/CEO</div>
    </div>

    <div class="divider"></div>

    <div class="contact">
      <div class="contact__row">
        <svg class="contact__icon" viewBox="0 0 24 24" aria-hidden="true"><path d="M6.6 10.8a15.1 15.1 0 0 0 6.6 6.6l2.2-2.2a1 1 0 0 1 1-.25 11.4 11.4 0 0 0 3.6.57 1 1 0 0 1 1 1V20a1 1 0 0 1-1 1A17 17 0 0 1 3 4a1 1 0 0 1 1-1h3.5a1 1 0 0 1 1 1c0 1.25.2 2.45.57 3.57a1 1 0 0 1-.25 1z"/></svg>
        <span>(617)555-0193</span>
      </div>
      <div class="contact__row">
        <svg class="contact__icon" viewBox="0 0 24 24" aria-hidden="true"><path d="M2 5h20v14H2z M2 5l10 8 10-8" fill="var(--brand-blue)"/><path d="M3 6l9 7 9-7" fill="none" stroke="#fff" stroke-width="1.6"/></svg>
        <span>dara@hollinledger.example</span>
      </div>
    </div>

    <div class="address">
      <div>2746 Marrow Lane</div>
      <div>Boston MA 02391</div>
    </div>

    <svg class="footer-band" width="616" height="352" viewBox="0 0 616 352" aria-hidden="true">
      <path d="M0 328 H360 V337 H0 Z" fill="var(--brand-green)"/>
      <path d="M340 352 C354 352 356 309 384 309 L616 309 L616 352 Z" fill="var(--brand-blue)"/>
    </svg>
    <div class="website">www.hollinledger.example</div>
  </section>

  <section class="card card--back" aria-label="Card back">
    <div class="wordmark"><span class="wordmark__mark"></span>Hollin Ledger</div>
  </section>
</body>
</html>
```